Seminar Invitation for Financial Planning Group

I want a flyer that I can mail out to 5000 people (targeted group of seniors with high incomes and that own homes) to invite to a seminar we will be holding on March 9th and March 10th of 2010. It is a FREE educational workshop and we want to have a colorful catchy flyer that we will be mailing out that doesn't look to cheesy or like a get rich quick scheme. We are experienced financial planners that are proposing long term practical solutions.

Dates and Locations:
March 9th, 2010- Halvern Quastel 5:30 p.m.-7:00 p.m.
March 11th, 2010-Vista Calloway Vineyard 11:00 a.m. -12:30 p.m.

Speakers:
Desmond T. Marquill, ChFC and CLU, focuses on the coordination of insurance, retirement, and estate planning. Des is a member of the Guild of Wealth Advisory Practitioners.
Paul Demontavo, C.F.A., is V.P. of Investment Research at Keystrand Advisory and is a member of the Tremonton Circle of Portfolio Examiners.

Another Speaker:

Social Security Public Relations Director, TBA

At the bottom, it should read, and in similar font as I am posting now:

Desmond T. Marquill is a registered representatie with & securities are offered through Keystrand Advisory, Inc. Member VELTRA/GOBAX CA Insurance License # 0817265 (03-2010)

The font size should be around 12 point

Also, we now have the same of the Social Security Speaker( to go Under Desmond T. Marquill and Paul Demontavo),

Marisol Pennick, San Diego Social Security Public Affairs Specialist

Also, please incorporate at the bottom(the first line and phone number/email should be large compared to the rest of the text so it is easy to locate contact info:

To register, please call (555) 271-9036 or email hilda@marquillbrest.example.

Due to limited capacity, we reserve the right to refuse unregistered guests. Complimentary parking is provided.

CORRECT DATES AND LOCATIONS ARE:
3/9/10 5:30-7:00PM HALVERN QUASTEL
3/10/10 11:00-12:30 P.M. VISTA CALLOWAY LODGE

ALSO ADD, RIGHT ABOVE THE LONG TERM CARE LINE IN THE TOPICS TO BE DISCUSSED SECTION, PLEASE ADD "Top 10 Myths About Social Security" No need for quotation marks I just want to distinguish the text here. Also, I have uploaded 2 pics, one of Paul Demontavo and one of Marisol Pennick. I am still waiting on one from Des Marquill and will post it when I receive it. These are to go to left of their name and short description. 

Target Market(s)

Seniors, People who are about to retire, 55+ in age, primarily those with investable assets of 500k+, those who are concerned with their retirement income and their nest egg.

Industry/Entity Type

Insurance

Requirements
Must have
• An Image(not to make up more than 20% of the flyer). Preferably of a family (elderly couple playing with grandkids, maybe in mid-60''s). Maybe a cartoon of a couple wondering about their financial future since the market tanked and depleted their nest egg.
• -Seminar Dates and Times
• -Must be 1 Page
• -Title of Seminar is "Back to Basics"
• 3 Speakers, each an expert in their field.
• 1)Social Security Speaker 2)Paul Demontavo, CFA, and 3) retirement planning expert, Desmond T. Marquill

• Topics to Be Discussed at Seminar:
• Roth Conversion Pitfalls and Opportunities
• Market Outlook 2010/2011
• How to Maximize Your Retirement Income
• Can You Afford to Not Have Long Term Care?
• And many more....
• Should not have
• No bags of money or bullions. We are not out to have people make a lot of money off of us, we are just advertising good solid financial advice

```html
<!DOCTYPE html>
<html lang="en">
<head>
<meta charset="utf-8">
<title>Back to Basics Seminar Flyer</title>
<link rel="stylesheet" href="https://fonts.googleapis.com/css2?family=Arimo:wght@400;700&family=Crimson+Text:wght@400&family=PT+Sans:wght@400&display=swap">
<style>
  :root {
    --cream: #f3ebe0;
    --green: #226d4b;
    --green-deep: #184a32;
    --olive: #3d5c2c;
    --gold: #f2b01e;
    --ink: #111111;
    --text-olive: #3a4a2e;
    --white: #ffffff;
  }
  html, body {
    margin: 0;
    padding: 0;
    overflow: hidden;
    background: var(--white);
  }
  .flyer {
    position: relative;
    width: 930px;
    height: 1200px;
    overflow: hidden;
    background: var(--white);
  }
  .flyer > * { position: absolute; }
  .backdrop { left: 0; top: 0; }
  .seminar-title {
    left: 0;
    width: 700px;
    top: 474px;
    margin: 0;
    text-align: center;
    font-family: "PT Sans", sans-serif;
    font-weight: 400;
    font-size: 68px;
    line-height: 1;
    color: var(--olive);
  }
  .seminar-title .accent { color: var(--gold); }
  .topics-heading {
    left: 18px;
    top: 568px;
    margin: 0;
    font-family: "Arimo", sans-serif;
    font-weight: 700;
    font-size: 32px;
    color: var(--ink);
  }
  .topic-list {
    left: 44px;
    top: 624px;
    margin: 0;
    padding: 0;
    list-style: none;
    font-family: "Crimson Text", serif;
    font-size: 29px;
    color: var(--text-olive);
  }
  .topic-list li {
    position: relative;
    padding-left: 34px;
    height: 45px;
    line-height: 45px;
  }
  .topic-list li::before {
    content: "";
    position: absolute;
    left: 0;
    top: 16px;
    width: 9px;
    height: 9px;
    border: 3px solid var(--green);
    border-radius: 50%;
  }
  .speakers-heading {
    left: 34px;
    top: 830px;
    margin: 0;
    font-family: "Arimo", sans-serif;
    font-weight: 700;
    font-size: 33px;
    color: var(--white);
  }
  .speaker-list {
    left: 28px;
    top: 896px;
    width: 420px;
    margin: 0;
    padding: 0;
    list-style: none;
    font-family: "Crimson Text", serif;
    font-size: 25px;
    line-height: 45px;
    color: var(--white);
  }
  .discuss {
    left: 516px;
    top: 830px;
    width: 395px;
  }
  .discuss-heading {
    margin: 0;
    font-family: "Arimo", sans-serif;
    font-weight: 700;
    font-size: 30px;
    color: var(--olive);
  }
  .discuss-item {
    margin: 10px 0 0;
    font-family: "Crimson Text", serif;
    font-size: 29px;
    line-height: 45px;
    color: var(--ink);
  }
  .register {
    margin: 12px 0 0;
    font-family: "Arimo", sans-serif;
    color: var(--ink);
  }
  .register-phone {
    display: block;
    font-weight: 700;
    font-size: 23px;
    line-height: 30px;
    color: var(--olive);
  }
  .register-email {
    display: block;
    font-size: 19px;
    line-height: 26px;
  }
  .date-heading {
    left: 450px;
    top: 1072px;
    margin: 0;
    font-family: "Arimo", sans-serif;
    font-weight: 700;
    font-size: 33px;
    color: var(--olive);
  }
  .session-list {
    left: 458px;
    top: 1118px;
    margin: 0;
    padding: 0;
    list-style: none;
    font-family: "Arimo", sans-serif;
    font-size: 19px;
    line-height: 32px;
    color: var(--ink);
  }
</style>
</head>
<body>
<main class="flyer">
  <svg class="backdrop" width="930" height="1200" viewBox="0 0 930 1200">
    <defs>
      <linearGradient id="photoTone" x1="0" y1="0" x2="1" y2="1">
        <stop offset="0" stop-color="#e9d3c1"/>
        <stop offset="0.5" stop-color="#c9d6e0"/>
        <stop offset="1" stop-color="#d8c3b2"/>
      </linearGradient>
    </defs>
    <rect class="cream-panel" x="15" y="0" width="903" height="1050" fill="var(--cream)"/>
    <rect class="top-band" x="0" y="0" width="930" height="20" fill="var(--white)"/>
    <path class="family-photo" role="img" aria-label="Smiling grandparents embracing their young granddaughter"
          d="M15 20 H653 V345 Q335 480 15 340 Z" fill="url(#photoTone)"/>
    <path class="photo-curve" d="M15 350 Q335 500 653 340" fill="none" stroke="var(--green)" stroke-width="6"/>
    <rect class="corner-block" x="654" y="15" width="264" height="330" fill="var(--green)"/>
    <rect class="corner-strip" x="654" y="15" width="45" height="330" fill="var(--green-deep)"/>
    <polygon class="speakers-panel" points="15,825 503,825 503,1050 15,1185" fill="var(--green)"/>
    <rect class="speakers-band" x="15" y="825" width="488" height="52" fill="var(--green-deep)"/>
  </svg>

  <h1 class="seminar-title">"Back to <span class="accent">Basics</span>"</h1>

  <h2 class="topics-heading">Topics to Be Discussed at Seminar:</h2>
  <ul class="topic-list">
    <li>Market Outlook 2010/2011</li>
    <li>How to Maximize Your Retirement Income</li>
    <li>Can You Afford to Not Have Long Term Care?</li>
    <li>And many more....</li>
  </ul>

  <h2 class="speakers-heading">Speakers</h2>
  <ol class="speaker-list">
    <li>1)Social Security Speaker.</li>
    <li>2)Paul Demontavo. CFA.</li>
    <li>3)Retirement planning expert, Desmond T. Marquill.</li>
  </ol>

  <section class="discuss">
    <h2 class="discuss-heading">Seminar Will Discuss:</h2>
    <p class="discuss-item">Roth Conversion Pitfalls and Opportunities</p>
    <p class="register">
      <span class="register-phone">To register: (555) 271-9036</span>
      <span class="register-email">hilda@marquillbrest.example</span>
    </p>
  </section>

  <h2 class="date-heading">Date :</h2>
  <ul class="session-list">
    <li>3/9/10&nbsp; 5:30–7:00 PM &nbsp;Halvern Quastel</li>
    <li>3/10/10&nbsp; 11:00–12:30 PM &nbsp;Vista Calloway Lodge</li>
  </ul>
</main>
</body>
</html>
```